Graphic to show easy steps to find financial clarity

Howdy-I need a graphic that describe my Coin Compass Method.The attached is a concept, but please use your own creativity to show how you would display this:- There are 5 steps the process (and then we repeat/recalculate)- And three bullets that drive home the results of the processI've also attached my logo. Please use the colors in my logo and maybe add a soft green as needed.The reader should be able to briefly scan this document and understand that this is an easy/simple process that tells them how to manage their cash.Thanks!-Ned

Target Market(s)

wealthy women, whether single or married

Requirements
Must have
• Please use the colors in my logo and a soft green if needed
Should not have
• This should be a very easy to read graphic that communicates how simple/easy this is to do.

```html
<!DOCTYPE html>
<html lang="en">
<head>
<meta charset="utf-8">
<title>Coin Compass Method</title>
<link href="https://fonts.googleapis.com/css2?family=Roboto:wght@400;500;700&display=swap" rel="stylesheet">
<style>
  :root {
    --bg: #cfcfcf;
    --navy: #0b3a7c;
    --white: #ffffff;
    --ink: #4a4a4a;
    --icon: #555555;
  }
  * { margin: 0; padding: 0; box-sizing: border-box; }
  html, body { width: 1200px; height: 800px; overflow: hidden; background: var(--bg); }
  .canvas {
    position: relative; width: 1200px; height: 800px; background: var(--bg);
    font-family: "Roboto", Arial, sans-serif; color: var(--ink);
  }
  .title-pill {
    position: absolute; left: 330px; top: 85px; width: 539px; height: 48px;
    background: var(--navy); border-radius: 14px;
    display: flex; align-items: center; justify-content: center;
    color: var(--white); font-weight: 700; font-size: 13px; letter-spacing: 0.42em;
    text-transform: uppercase;
  }
  .connector {
    position: absolute; left: 101px; top: 202px; width: 998px;
    border-top: 2px dashed var(--navy);
  }
  .step-number {
    position: absolute; top: 174px; width: 58px; height: 58px; margin-left: -29px;
    border-radius: 50%; background: var(--navy); color: var(--white);
    display: flex; align-items: center; justify-content: center;
    font-weight: 700; font-size: 22px;
  }
  .repeat-pill {
    position: absolute; left: 1027px; top: 180px; width: 146px; height: 51px;
    border-radius: 26px; background: var(--navy); color: var(--white);
    display: flex; align-items: center; justify-content: center;
    font-weight: 700; font-size: 24px; letter-spacing: 0.02em;
  }
  .step-card {
    position: absolute; top: 241px; width: 162px; height: 307px;
  }
  .step-card .banner { position: absolute; inset: 0; width: 162px; height: 307px; }
  .step-label {
    position: absolute; top: 50px; left: 16px; right: 16px;
    text-align: center; text-transform: uppercase; font-size: 17.5px; line-height: 24px;
    color: var(--ink);
  }
  .step-icon {
    position: absolute; top: 140px; left: 50%; margin-left: -32px; width: 64px; height: 64px;
  }
  .step-icon * { fill: none; stroke: var(--icon); stroke-width: 2.6; stroke-linecap: round; stroke-linejoin: round; }
  .step-icon .solid { fill: var(--icon); stroke: none; }
  .step-icon text { fill: var(--icon); stroke: none; font-family: "Roboto", Arial, sans-serif; font-weight: 500; }
  .result {
    position: absolute; left: 150px; width: 900px; height: 42px;
    display: flex; align-items: center; justify-content: center;
    text-transform: uppercase; font-size: 18.5px; letter-spacing: 0.01em; color: var(--ink);
    background: linear-gradient(90deg, rgba(255,255,255,0) 0%, rgba(255,255,255,0.75) 30%, rgba(255,255,255,0.75) 70%, rgba(255,255,255,0) 100%);
  }
</style>
</head>
<body>
<div class="canvas">
  <div class="title-pill">Coin Compass Method</div>

  <div class="connector"></div>
  <div class="step-number" style="left:101px">01</div>
  <div class="step-number" style="left:304px">02</div>
  <div class="step-number" style="left:505px">03</div>
  <div class="step-number" style="left:705px">04</div>
  <div class="step-number" style="left:906px">05</div>
  <div class="repeat-pill">REPEAT</div>

  <!-- Step 1 -->
  <div class="step-card" style="left:19px">
    <svg class="banner" viewBox="0 0 162 307"><polygon points="0,0 162,0 162,232 81,307 0,232" fill="#0b3a7c"/><polygon points="16,0 146,0 146,178 81,248 16,178" fill="#fff"/></svg>
    <div class="step-label">Know your annual spending</div>
    <svg class="step-icon" viewBox="0 0 64 64">
      <rect class="solid" x="6" y="42" width="9" height="16"/>
      <rect class="solid" x="20" y="34" width="9" height="24"/>
      <rect class="solid" x="34" y="38" width="9" height="20"/>
      <rect class="solid" x="48" y="26" width="9" height="32"/>
      <polyline points="4,40 20,26 34,32 58,14"/>
      <polyline points="50,14 58,14 58,22"/>
    </svg>
  </div>

  <!-- Step 2 -->
  <div class="step-card" style="left:222px">
    <svg class="banner" viewBox="0 0 162 307"><polygon points="0,0 162,0 162,232 81,307 0,232" fill="#0b3a7c"/><polygon points="16,0 146,0 146,178 81,248 16,178" fill="#fff"/></svg>
    <div class="step-label">Project special expenses</div>
    <svg class="step-icon" viewBox="0 0 64 64">
      <circle cx="34" cy="22" r="16"/>
      <text x="34" y="30" font-size="22" text-anchor="middle">$</text>
      <path d="M4 50 C14 42 22 42 30 46 L42 46 C46 46 46 52 42 52 L30 52"/>
      <path d="M42 50 L54 42 C58 40 61 44 58 47 L44 58 L8 58"/>
    </svg>
  </div>

  <!-- Step 3 -->
  <div class="step-card" style="left:422px">
    <svg class="banner" viewBox="0 0 162 307"><polygon points="0,0 162,0 162,232 81,307 0,232" fill="#0b3a7c"/><polygon points="16,0 146,0 146,178 81,248 16,178" fill="#fff"/></svg>
    <div class="step-label">Add up your 5-year cash needs</div>
    <svg class="step-icon" viewBox="0 0 64 64">
      <path d="M14 8 L44 8 L52 16 L52 58 L14 58 Z"/>
      <line x1="24" y1="24" x2="44" y2="24"/>
      <line x1="24" y1="32" x2="44" y2="32"/>
      <line x1="24" y1="40" x2="44" y2="40"/>
      <line x1="24" y1="48" x2="38" y2="48"/>
      <circle cx="12" cy="14" r="7" fill="#fff"/>
      <polyline points="9,14 11.5,16.5 15.5,11.5"/>
    </svg>
  </div>

  <!-- Step 4 -->
  <div class="step-card" style="left:623px">
    <svg class="banner" viewBox="0 0 162 307"><polygon points="0,0 162,0 162,232 81,307 0,232" fill="#0b3a7c"/><polygon points="16,0 146,0 146,178 81,248 16,178" fill="#fff"/></svg>
    <div class="step-label">Set them aside in savings</div>
    <svg class="step-icon" viewBox="0 0 64 64">
      <path d="M24 8 L40 8 L35 18 L29 18 Z"/>
      <path d="M28 18 C12 26 6 40 8 50 C10 58 18 60 32 60 C46 60 54 58 56 50 C58 40 52 26 36 18"/>
      <text x="32" y="50" font-size="22" text-anchor="middle">$</text>
    </svg>
  </div>

  <!-- Step 5 -->
  <div class="step-card" style="left:823px">
    <svg class="banner" viewBox="0 0 162 307"><polygon points="0,0 162,0 162,232 81,307 0,232" fill="#0b3a7c"/><polygon points="16,0 146,0 146,178 81,248 16,178" fill="#fff"/></svg>
    <div class="step-label">Invest the rest</div>
    <svg class="step-icon" viewBox="0 0 64 64">
      <text x="32" y="60" font-size="26" text-anchor="middle">$</text>
      <line x1="32" y1="36" x2="32" y2="6"/>
      <polyline points="27,11 32,6 37,11"/>
      <line x1="32" y1="36" x2="12" y2="18"/>
      <polyline points="12,25 12,18 19,18"/>
      <line x1="32" y1="36" x2="52" y2="18"/>
      <polyline points="45,18 52,18 52,25"/>
      <line x1="32" y1="36" x2="8" y2="34"/>
      <line x1="32" y1="36" x2="56" y2="34"/>
    </svg>
  </div>

  <!-- Repeat -->
  <div class="step-card" style="left:1018px">
    <svg class="banner" viewBox="0 0 162 307"><polygon points="0,0 162,0 162,232 81,307 0,232" fill="#0b3a7c"/><polygon points="16,0 146,0 146,178 81,248 16,178" fill="#fff"/></svg>
    <div class="step-label">Recalculate monthly</div>
    <svg class="step-icon" viewBox="0 0 64 64">
      <circle cx="32" cy="30" r="14"/>
      <text x="32" y="38" font-size="20" text-anchor="middle">$</text>
      <path d="M12 40 A22 22 0 0 1 28 8"/>
      <polyline points="22,5 28,8 24,14"/>
      <path d="M52 40 A22 22 0 0 1 40 51"/>
      <polygon class="solid" points="24,58 40,58 32,50"/>
      <polygon class="solid" points="10,48 18,52 14,44"/>
      <polygon class="solid" points="54,48 46,52 50,44"/>
    </svg>
  </div>

  <div class="result" style="top:598px">Know your lifestyle will be unaffected by the markets for at least 5-years</div>
  <div class="result" style="top:660px">Spend intentionally and with Ned</div>
  <div class="result" style="top:721px">Create a solid base for lifetime cash flow projections</div>
</div>
</body>
</html>
```